VORN - Business cards

Business card to be created for Commercial sales staff

Target Market(s)

Commercial businesses

Industry/Entity Type

Commercial

Contact Information for Business Card

Look professional. For commercial clients

Colors
ffffff

Requirements
Must have
• - Vorn Logo
• - Commercial sales staff as postion
• - room for commerical sales manager role
• - person name and their mobile number
• - Website : vornelectrical.com.au
Nice to have
• White background.
• On back of business card just have the logo no other information
Should not have
• Should only have white background on front of card.

```html
<!DOCTYPE html>
<html lang="en">
<head>
<meta charset="utf-8">
<title>VORN – Business Card</title>
<link href="https://fonts.googleapis.com/css2?family=Questrial&display=swap" rel="stylesheet">
<style>
  :root {
    --page-bg: #e9e6e1;
    --card-bg: #ffffff;
    --card-shade: #e4e4e6;
    --ink-dark: #2b2e34;
    --brand-red: #c4161c;
    --ink-text: #1f1f22;
  }
  html, body {
    margin: 0;
    padding: 0;
    width: 1200px;
    height: 892px;
    overflow: hidden;
    background: var(--page-bg);
  }
  .canvas {
    position: relative;
    width: 1200px;
    height: 892px;
    display: flex;
    align-items: center;
    justify-content: center;
  }
  .business-card {
    position: relative;
    width: 900px;
    height: 514px;
    background: linear-gradient(180deg, var(--card-bg) 0%, var(--card-bg) 35%, var(--card-shade) 100%);
    box-shadow: 0 18px 40px rgba(0,0,0,0.25);
    font-family: "Questrial", "Century Gothic", sans-serif;
  }
  .brand {
    position: absolute;
    left: 250px;
    top: 120px;
    display: flex;
    align-items: center;
    gap: 18px;
  }
  .brand-dot {
    width: 64px;
    height: 64px;
    border-radius: 50%;
    background: var(--brand-red);
  }
  .brand-name {
    font-size: 96px;
    line-height: 1;
    letter-spacing: 4px;
    color: var(--ink-dark);
  }
  .staff {
    position: absolute;
    left: 352px;
    top: 232px;
  }
  .staff-name {
    font-size: 34px;
    color: var(--brand-red);
    line-height: 1.1;
  }
  .staff-role {
    font-size: 15px;
    font-weight: 700;
    color: var(--ink-text);
    margin-left: 62px;
    letter-spacing: 0.5px;
  }
  .contact {
    position: absolute;
    left: 500px;
    top: 350px;
    font-size: 22px;
    color: var(--ink-text);
    line-height: 1.9;
    letter-spacing: 0.5px;
  }
</style>
</head>
<body>
  <main class="canvas">
    <section class="business-card" aria-label="VORN business card front">
      <div class="brand">
        <span class="brand-dot" aria-hidden="true"></span>
        <span class="brand-name">VORN</span>
      </div>
      <div class="staff">
        <div class="staff-name">Daniel Hart</div>
        <div class="staff-role">manager</div>
      </div>
      <div class="contact">
        <div class="contact-phone">214-555-0182</div>
        <div class="contact-web">vornelectrical.com.au</div>
      </div>
    </section>
  </main>
</body>
</html>
```